Mental Health and Marriage & Family Counseling Office Business Card Design

I work with a wide range of emotional and behavioral issues providing services that span from therapy for depression and grief counseling to parenting support, couples counseling and beyond. In a comfortable and supportive atmosphere, I offer a highly personalized approach tailored to each of my clients individual needs to help attain the personal growth they’re striving for. Providing individual, couples and family counseling.
Treatment specialization includes: Therapy for Depression and Anxiety, Couples Counseling, Family Counseling, Parenting Support, Grief Counseling, Work and Career issues, Stress Management, Conflict Resolution. I would like to see designs that use the colors "of a Peacock feather" , such as blues and greens, etc.

Industry/Entity Type

Business

Contact Information for Business Card

Delia K. Fenwick, MS, LPC
Licensed Professional Counselor
415 Harrowgate Lane Suite 231
Jacksonville, NC 28593

(910) 487-6124 Fax: (910) 487-6125
www.deliafenwicklpc.example
delia@deliafenwicklpc.example

```html
<!DOCTYPE html>
<html lang="en">
<head>
<meta charset="utf-8">
<title>Delia K. Fenwick, MS, LPC – Business Card</title>
<link rel="stylesheet" href="https://fonts.googleapis.com/css2?family=Mulish:wght@400;800&family=Open+Sans:wght@400;600&display=swap">
<style>
  :root {
    --bg: #e4e5e6;
    --card: #ffffff;
    --blue: #0d4f9e;
    --green: #3aa637;
    --lime: #7dc242;
    --ink: #3a3a3a;
    --rule: #e2e2e2;
  }
  * { box-sizing: border-box; margin: 0; padding: 0; }
  html, body { width: 1200px; height: 852px; overflow: hidden; }
  body { background: var(--bg); font-family: "Open Sans", sans-serif; color: var(--ink); position: relative; }

  .card {
    position: absolute; width: 525px; height: 300px;
    background: var(--card); border-radius: 18px; overflow: hidden;
    box-shadow: 0 6px 18px rgba(0,0,0,.18);
  }
  .card--front { left: 150px; top: 96px; }
  .card--back { left: 525px; top: 452px; }

  .brand { display: flex; align-items: center; gap: 12px; }
  .brand__dot { width: 30px; height: 30px; border-radius: 50%; background: var(--blue); flex: none; }
  .brand__name { font-family: "Mulish", sans-serif; font-weight: 800; color: var(--blue); font-size: 27px; line-height: 1.05; letter-spacing: -.3px; }
  .brand__tagline { font-family: "Mulish", sans-serif; font-weight: 400; color: var(--green); font-size: 15px; margin-top: 3px; }

  .card--front .brand { position: absolute; left: 50%; top: 50%; transform: translate(-50%, -50%); white-space: nowrap; }

  .card--back .brand { position: absolute; left: 30px; top: 30px; }
  .card--back .brand__name { font-size: 25px; }
  .card--back .brand__tagline { font-size: 14px; }

  .divider { position: absolute; left: 262px; top: 108px; width: 1px; height: 120px; background: var(--rule); }

  .person { position: absolute; left: 30px; top: 126px; width: 220px; text-align: center; }
  .person__name { font-family: "Mulish", sans-serif; font-weight: 800; color: var(--blue); font-size: 17px; }
  .person__title { font-size: 11.5px; margin-top: 1px; }
  .person__address { font-size: 12.5px; margin-top: 18px; line-height: 1.45; }

  .contact { position: absolute; left: 282px; top: 116px; list-style: none; font-size: 11.5px; }
  .contact li { display: flex; align-items: center; gap: 9px; height: 19px; }
  .contact svg { width: 12px; height: 12px; fill: var(--lime); flex: none; }
  .contact .accent { color: var(--lime); }

  .band { position: absolute; left: 0; bottom: 0; width: 525px; height: 70px; }
</style>
</head>
<body>

<section class="card card--front" aria-label="Card front">
  <div class="brand">
    <span class="brand__dot"></span>
    <div>
      <div class="brand__name">Delia K. Fenwick, MS, LPC</div>
      <div class="brand__tagline">Therapy for Individuals, Couples &amp; Families</div>
    </div>
  </div>
</section>

<section class="card card--back" aria-label="Card back">
  <div class="brand">
    <span class="brand__dot"></span>
    <div>
      <div class="brand__name">Delia K. Fenwick, MS, LPC</div>
      <div class="brand__tagline">Therapy for Individuals, Couples &amp; Families</div>
    </div>
  </div>

  <div class="person">
    <div class="person__name">Delia K. Fenwick, MS</div>
    <div class="person__title">Licensed Professional Counselor</div>
    <div class="person__address">415 Harrowgate Lane Suite<br>231 Jacksonville, NC 28593</div>
  </div>

  <div class="divider"></div>

  <ul class="contact">
    <li><svg viewBox="0 0 12 12"><path d="M1 4c0-2 2-3 5-3s5 1 5 3l-2 1-1-2H4L3 5zM3 6h6l1 5H2z"/></svg>(910) 487-6124</li>
    <li><svg viewBox="0 0 12 12"><path d="M3 1h5v3H3zM1 5h10v6H1zM3 7v2h6V7z"/></svg>(910) 487-6125</li>
    <li><svg viewBox="0 0 12 12"><path d="M6 1a5 5 0 100 10A5 5 0 006 1zm-3 4h6v2H3z"/></svg>www.<span class="accent">deliafenwicklpc</span>.example</li>
    <li><svg viewBox="0 0 12 12"><path d="M1 3h10v7H1zm1 1l4 3 4-3z" fill-rule="evenodd"/></svg>delia@deliafenwicklpc.example</li>
  </ul>

  <svg class="band" viewBox="0 0 525 70" preserveAspectRatio="none" aria-hidden="true">
    <polygon points="330,26 525,0 525,70 330,70" fill="var(--lime)"/>
    <polygon points="0,58 355,22 525,18 525,70 0,70" fill="var(--blue)"/>
    <polygon points="0,70 0,58 355,22 525,18 525,22 360,28 0,64" fill="#ffffff" opacity=".25"/>
  </svg>
</section>

</body>
</html>
```